Web Design Project

We are a SaaS company that specializes in the thrift industry POS and inventory software. We want a clean and professional site that does NOT look like a template site.

*** A little more about our business -
We offer a SaaS (Software As A Service) for a Point Of Sale and inventory control product specifically for the Thrift / Second hand industry. The software allows them to process inventory, grade/rate it, create the barcoded tags. It the does the whole retail sale process. We also offer tie-ins to Pixelyard, Chirpnest and apple/droid mobile apps to support our customers thrift stores.

We need to in incorporate the look/feel and color scheme of our logo.

I would imagine possibly a HTML5 slideshow (3-5 slides) rotating on the home page showing screenshots, etc.

I am envisioning icons representing features of our product.

PLEASE ask questions, I am sure I have left out a ton.
Updates

Requirements
Must have
• I have attached a couple of our logo's with color options. It needs to flow with that.

I have also attached a screen shot of what I think might work. This DOESN'T suggest that is what I am looking for, just a sample.

I am thinking a home page and maybe one or two sub pages
***Update, I kind of like the following concept for one of the sub-pages
http://www.quotivex.example/estimate.html

There should also be a place to highlight Pixelyard and chirpnest.

It will be a bilingual / multilingual site, so take that into account
Should not have
• I don't want it to look like a template site. It should be clean and professional.

```html
<!DOCTYPE html>
<html lang="en">
<head>
<meta charset="utf-8">
<title>Resale Compass – POS Store Front</title>
<link href="https://fonts.googleapis.com/css2?family=Roboto+Condensed:wght@300;400&family=Arimo:wght@400;700&display=swap" rel="stylesheet">
<style>
:root{
  --blue:#1a9ad6;
  --blue-dark:#0f6f9f;
  --blue-deep:#0b5b86;
  --blue-mid:#12719f;
  --ink:#222;
  --grey-text:#666;
  --bar:#222;
  --footer:#1b1b1b;
  --footer-box:#242424;
  --link:#1a9ad6;
  --cyan:#7fd4f7;
}
*{box-sizing:border-box;margin:0;padding:0}
html,body{width:1013px;height:1200px;overflow:hidden;background:#1b1b1b}
body{font-family:"Arimo",Arial,sans-serif;color:var(--ink)}
.page{position:relative;width:1000px;height:1185px;transform:scale(1.013);transform-origin:0 0;background:#fff}
.abs{position:absolute}

/* top bar */
.topbar{left:0;top:0;width:1000px;height:42px;background:var(--bar);color:#fff;font-size:12.5px}
.topbar .item{position:absolute;top:0;height:42px;line-height:42px;padding:0 14px}
.topbar .lang{left:10px;width:87px;border-right:1px solid #333}
.topbar .service{left:98px;width:120px;background:#2c2c2c;border-right:1px solid #333}
.topbar .phone{left:218px}
.topbar .login{right:12px}

/* header */
.header{left:0;top:42px;width:1000px;height:86px;background:linear-gradient(#fff 70%,#eee)}
.brand{left:25px;top:20px;display:flex;align-items:center;gap:10px}
.brand .mark{width:44px;height:44px;background:var(--blue);border-radius:6px}
.brand .name{font-family:"Arimo",sans-serif;font-weight:700;font-size:29px;color:var(--blue);letter-spacing:-.5px}
.nav{right:10px;top:0;height:86px;display:flex;align-items:center}
.nav a{font-family:"Roboto Condensed",sans-serif;font-size:17px;color:#333;text-decoration:none;padding:0 20px;border-left:1px solid #eee;line-height:30px}
.nav a:first-child{border-left:none}
.nav a.active{color:var(--blue)}
.nav a.active span{border-bottom:2px solid var(--blue);padding-bottom:5px}

/* hero band */
.band{left:0;top:128px;width:1000px;height:420px;background:var(--blue)}
.search{left:10px;top:142px;width:294px;height:36px;background:#7cc6ea;border-radius:3px;padding:4px}
.search .field{position:absolute;left:4px;top:4px;width:262px;height:28px;background:#fff;font-size:12px;line-height:28px;padding-left:9px;color:#222}
.search .btn{position:absolute;right:4px;top:4px;width:28px;height:28px;background:#fff;border-left:1px solid #ddd}

.tools{left:10px;top:187px;width:294px;height:335px;background:var(--blue-mid)}
.tools .head{height:36px;background:var(--blue-deep);color:#fff;font-family:"Roboto Condensed",sans-serif;font-size:17px;line-height:36px;padding-left:15px;position:relative}
.tools .row{height:36px;margin-top:3px;background:#1579aa;color:#a9d6ee;font-family:"Roboto Condensed",sans-serif;font-size:15px;line-height:36px;padding-left:49px;position:relative}
.tools .row svg.cart{position:absolute;left:17px;top:9px}
.tools .row .caret{position:absolute;right:16px;top:13px}
.tools ul{list-style:none;padding:8px 0 6px 27px;background:var(--blue-mid)}
.tools li{font-size:12px;color:#fff;line-height:21px;position:relative;padding-left:18px}
.tools li::before{content:"";position:absolute;left:0;top:6px;width:9px;height:9px;border-radius:50%;background:#e6eef3}

.crumbs{left:320px;top:142px;width:670px;height:35px;background:#fff;border-radius:2px;display:flex;align-items:center;padding-left:13px;font-size:12px;color:#555;gap:10px}
.crumbs .home{width:22px;height:18px;background:var(--blue);border-radius:3px}

.slide{left:320px;top:187px;width:670px;height:335px;background:linear-gradient(120deg,#b9a37e 0%,#5d6f86 35%,#7b8aa0 60%,#c9cfbc 85%,#e7dfd2 100%)}
.caption{position:absolute;left:0;bottom:0;width:670px;height:66px;background:rgba(10,10,10,.85);color:#fff;font-size:14px}
.caption .title{position:absolute;left:18px;top:13px}
.caption .links{position:absolute;left:40px;top:34px;display:flex;align-items:center;gap:18px}

/* content */
.content{left:10px;top:538px;width:980px;height:392px;background:#fff;border-radius:4px 4px 0 0}
.intro{left:25px;top:552px;width:950px;font-family:"Roboto Condensed",sans-serif;font-weight:300;font-size:18px;line-height:25px;color:#222}
.video{left:25px;top:615px;width:279px;height:237px;background:#111}
.video .shot{position:absolute;left:2px;top:2px;width:275px;height:208px;background:linear-gradient(135deg,#7c8a99,#c8cdd3 45%,#e7e3dd 70%,#b84c3c)}
.video .controls{position:absolute;left:0;bottom:0;width:279px;height:25px;background:#1d1d1d;color:#ccc;font-size:8px;display:flex;align-items:center;gap:10px;padding-left:14px}
.card{top:615px;width:202px}
.card .thumb{width:202px;height:146px;border:1px solid #ddd;padding:6px;background:#fff;box-shadow:0 1px 2px rgba(0,0,0,.1)}
.card .thumb div{width:100%;height:100%}
.card h3{font-size:12px;font-weight:700;color:var(--link);margin-top:9px}
.card p{font-size:12px;line-height:16px;color:var(--grey-text);margin-top:7px;text-align:justify}

/* footer */
.footer{left:0;top:928px;width:1000px;height:208px;background:var(--footer)}
.fbox{top:928px;width:300px;height:188px;background:var(--footer-box);border:1px solid #111;border-top:none;padding:15px 14px;color:#bbb;font-size:12px;line-height:18px}
.fbox h4{font-family:"Roboto Condensed",sans-serif;font-weight:400;font-size:19px;color:#eee;padding-bottom:6px;border-bottom:1px solid #555;width:160px;margin-bottom:15px}
.fbox .icon{position:absolute;right:10px;top:10px}
.fbox .date{color:var(--cyan)}
.fbox .more{color:var(--cyan);display:block;margin-top:4px}
.subscribe{height:34px;background:#111;border-radius:3px;padding:3px;display:flex;margin-bottom:10px;margin-top:-3px}
.subscribe .input{flex:1;background:#ccc}
.subscribe .go{width:95px;background:var(--blue);color:#fff;font-weight:700;font-size:16px;text-align:center;line-height:28px}
.copy{left:0;top:1136px;width:1000px;height:49px;background:#111;color:#ccc;font-size:12px;text-align:center;line-height:49px}
</style>
</head>
<body>
<div class="page">

  <div class="abs topbar">
    <div class="item lang">English
      <svg width="9" height="6" viewBox="0 0 9 6" style="margin-left:6px"><path d="M1 1l3.5 3.5L8 1" fill="none" stroke="#ccc" stroke-width="1.3"/></svg>
    </div>
    <div class="item service">Cutomer Service</div>
    <div class="item phone">Call Us : 555.010.0199</div>
    <div class="item login">Register / Login</div>
  </div>

  <header class="abs header">
    <div class="abs brand"><span class="mark"></span><span class="name">resalecompass</span></div>
    <nav class="abs nav">
      <a class="active" href="#"><span>Home</span></a>
      <a href="#">About Us</a>
      <a href="#">Customers</a>
      <a href="#">Pricing</a>
      <a href="#">Solutions</a>
      <a href="#">Contact Us</a>
    </nav>
  </header>

  <div class="abs band"></div>

  <div class="abs search">
    <div class="field">Search</div>
    <div class="btn"><svg width="28" height="28" viewBox="0 0 28 28"><circle cx="12" cy="12" r="6.5" fill="none" stroke="#1a9ad6" stroke-width="2"/><path d="M17 17l6 6" stroke="#1a9ad6" stroke-width="2.5"/></svg></div>
  </div>

  <aside class="abs tools">
    <div class="head">Quick Tools
      <svg class="abs" style="right:14px;top:15px" width="14" height="8" viewBox="0 0 14 8"><path d="M0 0h14L7 8z" fill="#fff"/></svg>
    </div>
    <div class="row"><svg class="cart" width="22" height="18" viewBox="0 0 22 18"><path d="M1 2h4l3 10h10l2-7H6" fill="none" stroke="#a9d6ee" stroke-width="1.6"/><circle cx="9" cy="15.5" r="1.6" fill="#a9d6ee"/><circle cx="16" cy="15.5" r="1.6" fill="#a9d6ee"/></svg>POS Store Front<svg class="caret" width="7" height="12" viewBox="0 0 7 12"><path d="M0 0l7 6-7 6z" fill="#a9d6ee"/></svg></div>
    <div class="row"><svg class="cart" width="22" height="18" viewBox="0 0 22 18"><path d="M1 2h4l3 10h10l2-7H6" fill="none" stroke="#a9d6ee" stroke-width="1.6"/><circle cx="9" cy="15.5" r="1.6" fill="#a9d6ee"/><circle cx="16" cy="15.5" r="1.6" fill="#a9d6ee"/></svg>POS Store Front<svg class="caret" style="top:15px" width="12" height="7" viewBox="0 0 12 7"><path d="M0 0h12L6 7z" fill="#a9d6ee"/></svg></div>
    <ul>
      <li>Lorem Ipsum is simply dummy</li>
      <li>Lorem Ipsum is simply dummy</li>
      <li>Lorem Ipsum is simply dummy</li>
      <li>Lorem Ipsum is simply dummy</li>
    </ul>
    <div class="row" style="margin-top:0"><svg class="cart" width="22" height="18" viewBox="0 0 22 18"><path d="M1 2h4l3 10h10l2-7H6" fill="none" stroke="#a9d6ee" stroke-width="1.6"/><circle cx="9" cy="15.5" r="1.6" fill="#a9d6ee"/><circle cx="16" cy="15.5" r="1.6" fill="#a9d6ee"/></svg>POS Store Front<svg class="caret" width="7" height="12" viewBox="0 0 7 12"><path d="M0 0l7 6-7 6z" fill="#a9d6ee"/></svg></div>
    <div class="row"><svg class="cart" width="22" height="18" viewBox="0 0 22 18"><path d="M1 2h4l3 10h10l2-7H6" fill="none" stroke="#a9d6ee" stroke-width="1.6"/><circle cx="9" cy="15.5" r="1.6" fill="#a9d6ee"/><circle cx="16" cy="15.5" r="1.6" fill="#a9d6ee"/></svg>POS Store Front<svg class="caret" width="7" height="12" viewBox="0 0 7 12"><path d="M0 0l7 6-7 6z" fill="#a9d6ee"/></svg></div>
    <div class="row"><svg class="cart" width="22" height="18" viewBox="0 0 22 18"><path d="M1 2h4l3 10h10l2-7H6" fill="none" stroke="#a9d6ee" stroke-width="1.6"/><circle cx="9" cy="15.5" r="1.6" fill="#a9d6ee"/><circle cx="16" cy="15.5" r="1.6" fill="#a9d6ee"/></svg>POS Store Front<svg class="caret" width="7" height="12" viewBox="0 0 7 12"><path d="M0 0l7 6-7 6z" fill="#a9d6ee"/></svg></div>
  </aside>

  <div class="abs crumbs">
    <span class="home"></span>
    <svg width="7" height="11" viewBox="0 0 7 11"><path d="M1 1l4.5 4.5L1 10" fill="none" stroke="#1a9ad6" stroke-width="2"/></svg>
    <span>Quick Tools</span>
    <svg width="7" height="11" viewBox="0 0 7 11"><path d="M1 1l4.5 4.5L1 10" fill="none" stroke="#1a9ad6" stroke-width="2"/></svg>
    <span>POS Store Front</span>
    <svg width="7" height="11" viewBox="0 0 7 11"><path d="M1 1l4.5 4.5L1 10" fill="none" stroke="#1a9ad6" stroke-width="2"/></svg>
    <span>Lorem Ipsum is simply dummy</span>
  </div>

  <section class="abs slide" role="img" aria-label="Photo of a card payment terminal on a shop counter">
    <div class="caption">
      <div class="title">Our POS Systems</div>
      <div class="links">
        <span>Hardware</span>
        <svg width="16" height="16" viewBox="0 0 16 16"><path d="M8 1v14M1 8h14" stroke="#fff" stroke-width="3.5"/></svg>
        <span>Software</span>
        <svg width="16" height="16" viewBox="0 0 16 16"><path d="M8 1v14M1 8h14" stroke="#fff" stroke-width="3.5"/></svg>
        <span>Payment Processing</span>
        <svg width="16" height="16" viewBox="0 0 16 16"><path d="M8 1v14M1 8h14" stroke="#fff" stroke-width="3.5"/></svg>
        <span>Services</span>
      </div>
    </div>
  </section>

  <main class="abs content"></main>
  <p class="abs intro">Lorem Ipsum is simply dummy text of the printing and typesetting industry. Lorem Ipsum has been the industry's standard dummy text ever since the 1500s, when an unknown printer took a galley of type.</p>

  <div class="abs video">
    <div class="shot" role="img" aria-label="Video still of a card being swiped at a payment terminal"></div>
    <div class="controls">
      <svg width="8" height="9" viewBox="0 0 8 9"><path d="M0 0h3v9H0zM5 0h3v9H5z" fill="#ccc"/></svg>
      <svg width="12" height="10" viewBox="0 0 12 10"><path d="M0 3h3l4-3v10L3 7H0z" fill="#ccc"/></svg>
      <span>00:00 / 10:00</span>
    </div>
  </div>

  <article class="abs card" style="left:319px">
    <div class="thumb"><div role="img" aria-label="Photo of a phone tapped on a contactless reader" style="background:linear-gradient(135deg,#d9d6d2,#9a8e84 50%,#e9eaea)"></div></div>
    <h3>Lorem Ipsum is simply dummy</h3>
    <p>Lorem Ipsum is simply dummy text of the printing and typesetting industry. Lorem Ipsum has been the industry's standard dummy text ever since the 1500s, when an unknown printer took a galley of type and scrambled it to make a type specimen book.</p>
  </article>
  <article class="abs card" style="left:547px">
    <div class="thumb"><div role="img" aria-label="Photo of a shopper using a phone among clothing racks" style="background:linear-gradient(135deg,#c85a6a,#d9b9a6 45%,#3aa6b9 80%)"></div></div>
    <h3>Lorem Ipsum is simply dummy</h3>
    <p>Lorem Ipsum is simply dummy text of the printing and typesetting industry. Lorem Ipsum has been the industry's standard dummy text ever since the 1500s, when an unknown printer took a galley of type and scrambled it to make a type specimen book.</p>
  </article>
  <article class="abs card" style="left:775px">
    <div class="thumb"><div role="img" aria-label="Photo of a card terminal inside a small shopping cart" style="background:linear-gradient(#f2f2f2,#d8d8d8)"></div></div>
    <h3>Lorem Ipsum is simply dummy</h3>
    <p>Lorem Ipsum is simply dummy text of the printing and typesetting industry. Lorem Ipsum has been the industry's standard dummy text ever since the 1500s, when an unknown printer took a galley of type and scrambled it to make a type specimen book.</p>
  </article>

  <footer class="abs footer"></footer>
  <section class="abs fbox" style="left:30px">
    <svg class="icon" width="34" height="34" viewBox="0 0 34 34"><path d="M4 30l3-9L25 3l6 6L13 27z" fill="#777"/><path d="M4 30l3-9 6 6z" fill="#555"/></svg>
    <h4>Recent Blog Posts</h4>
    <div class="date">9/1/2012</div>
    <div>Lorem Ipsum is simply dummy text of&nbsp; the printing and typesetting industry.</div>
  </section>
  <section class="abs fbox" style="left:350px">
    <svg class="icon" width="40" height="32" viewBox="0 0 40 32"><path d="M4 4h32v18H18l-8 7v-7H4z" fill="#777"/></svg>
    <h4>Recent Chirpnest</h4>
    <div><span class="date">about 8 hours ago</span> Lorem Ipsum is simply dummy text of the printing and typesetting industry. Lorem Ipsum has been the industry's standard dummy text ever since the 1500s, when an unknown printer took a galley of type and scrambled.</div>
    <span class="more">There are many</span>
  </section>
  <section class="abs fbox" style="left:670px">
    <svg class="icon" width="42" height="34" viewBox="0 0 42 34"><path d="M2 14L21 2l19 12v18H2z" fill="#777"/><path d="M2 14l19 12 19-12" fill="none" stroke="#333" stroke-width="2"/></svg>
    <h4>Subscribe to Updates</h4>
    <div class="subscribe"><div class="input"></div><div class="go">Subscribe</div></div>
    <div>Lorem Ipsum is simply dummy text of the printing and typesetting industry. Lorem Ipsum has been the industry's standard dummy text ever since the 1500s,</div>
  </section>

  <div class="abs copy">Copyright @ 2012, Resale Compass. All Rights Reserved</div>
</div>
</body>
</html>
```